Q7 Teaser

One page teaser for our business information and model. A financial service SPV platform.

Target Market(s)

Financial Professionals

Industry/Entity Type

Financial Service

Font styles to use
Sans Serif

Colors
ffcf3e
ffffff
cfcfcf
9d9d9d
aaaaaa
fbed22
ffc214
fee18a
fbee3f

Requirements
Must have
• Unique appearance of USPs.
• Important claims: Low Cost. First Class.
• and: We liberate the buy-side from the sell-side
Nice to have
• maybe keyword cloud

```html
<!DOCTYPE html>
<html lang="en">
<head>
<meta charset="utf-8">
<title>Q7 Teaser</title>
<link rel="stylesheet" href="https://fonts.googleapis.com/css2?family=Jost:wght@300;400;500;600&family=Roboto+Condensed:wght@400;700&display=swap">
<style>
:root{
  --gold:#d39c1c;
  --gold-deep:#b9860f;
  --ink:#4a4a4a;
  --slate:#555555;
  --panel:#ececec;
  --white:#ffffff;
  --stage:#e6e6e8;
  --photo-dark:#3a2a14;
  --photo-mid:#8a6420;
  --photo-light:#e0b44a;
}
*{margin:0;padding:0;box-sizing:border-box}
html,body{width:1041px;height:1200px;overflow:hidden;background:var(--stage)}
.flyer{position:absolute;left:110px;top:20px;width:820px;height:1159px;background:var(--white);overflow:hidden;font-family:"Jost",sans-serif;color:var(--ink);box-shadow:0 6px 24px rgba(0,0,0,.18)}
.hero{position:absolute;left:0;top:0;width:820px;height:498px;background:
  radial-gradient(circle at 48% 47%,#f3e6c4 0 5%,transparent 14%),
  radial-gradient(ellipse at 80% 40%,var(--photo-light) 0,transparent 45%),
  linear-gradient(135deg,#d8d2c4 0%,var(--photo-mid) 35%,var(--photo-dark) 60%,var(--photo-mid) 85%,#c99a3a 100%)}
.hero-cap{position:absolute;left:0;top:0}
.brand{position:absolute;left:22px;top:38px;display:flex;align-items:center;gap:14px}
.brand-dot{width:58px;height:58px;border-radius:50%;background:var(--gold)}
.brand-name{font-family:"Jost",sans-serif;font-weight:400;font-size:30px;letter-spacing:1px;color:var(--gold)}
.claim{position:absolute;right:42px;top:246px;text-align:right;color:var(--white)}
.claim h1{font-family:"Jost",sans-serif;font-weight:600;font-size:47px;line-height:52px;letter-spacing:.5px;text-shadow:0 1px 4px rgba(0,0,0,.35)}
.claim p{font-weight:300;font-size:28px;line-height:31px;margin-top:12px;text-shadow:0 1px 4px rgba(0,0,0,.35)}
.banner{position:absolute;left:0;top:498px;width:820px;height:53px;background:var(--gold);color:var(--white);font-family:"Roboto Condensed",sans-serif;font-weight:700;font-size:29px;line-height:53px;text-align:center;letter-spacing:.3px}
.intro{position:absolute;left:0;top:551px;width:820px;height:139px;background:var(--slate);color:var(--white);padding:11px 26px 0 34px;font-size:13.4px;line-height:16.4px;text-align:justify;font-weight:400}
.usp{position:absolute;left:0;top:690px;width:439px;height:469px;background:var(--white)}
.usp-head{position:absolute;left:34px;top:12px;display:flex;align-items:flex-start}
.usp-your{font-weight:600;font-size:84px;line-height:80px;color:var(--gold);letter-spacing:1px}
.usp-words{margin-left:10px;margin-top:4px;font-weight:400;font-size:23px;line-height:23px;color:var(--ink)}
.ticks{list-style:none;position:absolute;font-size:15.8px;line-height:18px}
.ticks li{position:relative;padding-left:18px;margin-bottom:7px}
.ticks li::before{content:"";position:absolute;left:1px;top:4px;width:5px;height:9px;border:solid var(--gold);border-width:0 2px 2px 0;transform:rotate(40deg)}
.ticks-a{left:34px;top:114px;width:170px}
.ticks-b{left:213px;top:112px;width:215px}
.about{position:absolute;left:34px;top:358px;width:375px;font-size:15.2px;line-height:18px;text-align:justify}
.offer{position:absolute;left:439px;top:690px;width:381px;height:336px;background:var(--panel)}
.offer h2{position:absolute;left:35px;top:12px;font-family:"Roboto Condensed",sans-serif;font-weight:700;font-size:29px;color:var(--gold);letter-spacing:.4px}
.offer h3{position:absolute;left:35px;top:48px;font-weight:400;font-size:21px;color:var(--ink)}
.ticks-c{left:35px;top:94px;width:330px;font-size:16px}
.ticks-c li{margin-bottom:5px}
.contact{position:absolute;left:439px;top:1026px;width:381px;height:88px;background:var(--slate);text-align:center}
.contact h2{font-family:"Jost",sans-serif;font-weight:500;font-size:28px;color:var(--white);margin-top:8px;letter-spacing:.5px}
.phone{display:flex;justify-content:center;align-items:center;gap:12px;font-family:"Jost",sans-serif;font-weight:600;font-size:37px;line-height:40px;color:var(--gold)}
.footer{position:absolute;left:439px;top:1117px;width:381px;height:42px;background:var(--gold);color:var(--white);font-size:15.5px;display:flex;justify-content:center;align-items:center;gap:18px}
.footer span{display:flex;align-items:center;gap:7px}
</style>
</head>
<body>
<main class="flyer">
  <section class="hero" role="img" aria-label="Photograph looking up through a wooden lattice tower with golden light between the slats"></section>
  <svg class="hero-cap" width="420" height="160" viewBox="0 0 420 160" aria-hidden="true"><path d="M0 0H405C360 70 250 135 0 150Z" fill="#fff"/></svg>
  <div class="brand"><span class="brand-dot"></span><span class="brand-name">Q7 Financial Products</span></div>
  <div class="claim">
    <h1>LOW COST<br>FIRST CLASS</h1>
    <p>We democratise<br>structured financial<br>product issuance.</p>
  </div>

  <div class="banner">WE LIBERATE THE BUY-SIDE FROM THE SELL-SIDE.</div>

  <p class="intro">We serve our clients with the power to create their own branded, tailor-made financial products and investment solutions by providing them with right tools and structures to establish and operate first class off-balance sheet issuance vehicles (SPV). We create unique solutions to expand your business reach, services and qualities by liberating financial product issuance to buy-side. Asset owners, distributers and managers are given the full capability to securitise their own asset base in unlimited capacity, outside their balance sheet with customisable transparency and counterparty risk. A clear and simple solutions to serve your best interests and without the need for conventional sell-side issuers.</p>

  <section class="usp">
    <div class="usp-head"><span class="usp-your">YOUR</span><span class="usp-words">BRAND.<br>REWARD.<br>SOLUTION.</span></div>
    <ul class="ticks ticks-a">
      <li>Off-balance sheet</li>
      <li>Own issuance vehicle (SPV)</li>
      <li>Regulatory compliant (MIFID)</li>
      <li>Swiss Paying Agent</li>
      <li>Various off-shore locations</li>
      <li>Open Architecture</li>
      <li>Daily Liquidity</li>
    </ul>
    <ul class="ticks ticks-b">
      <li>Customised Transparency</li>
      <li>Low cost structure</li>
      <li>Your own fee policy</li>
      <li>Investment &amp; risk control</li>
      <li>Quick setup</li>
      <li>Transparent secondary market</li>
      <li>Full transparent pricing</li>
    </ul>
    <p class="about">Q7 Financial Product AG is a financial service provider built on the unique experience and robust track record of its team. Our founders gathered the most qualified experts to benefit our clients and business partners.</p>
  </section>

  <section class="offer">
    <h2>GROW YOUR BUSINESS</h2>
    <h3>OFFER YOUR PRODUCTS:</h3>
    <ul class="ticks ticks-c">
      <li>Structured Products</li>
      <li>Active Managed Certificate (AMC)</li>
      <li>Static Trackers</li>
      <li>Securitisation of depth</li>
      <li>Crypto-backed securities</li>
      <li>Trade Financial</li>
      <li>Asset backed Sec.</li>
      <li>Privat Equity Finance</li>
      <li>Insurance Linked Securities</li>
      <li>Leverage Products</li>
    </ul>
  </section>

  <section class="contact">
    <h2>CONTACT US TODAY</h2>
    <div class="phone">
      <svg width="26" height="22" viewBox="0 0 26 22" aria-hidden="true"><path d="M2 8C2 3 24 3 24 8L20 10 18 7H8L6 10Z" fill="#d39c1c"/><path d="M7 11H19L22 20H4Z" fill="#d39c1c"/><circle cx="13" cy="15" r="2.5" fill="#555"/></svg>
      <span>123-456-789</span>
    </div>
  </section>

  <footer class="footer">
    <span><svg width="11" height="11" viewBox="0 0 12 12" aria-hidden="true"><circle cx="6" cy="6" r="5" fill="none" stroke="#fff" stroke-width="1.4"/><path d="M1 6H11M6 1C3 4 3 8 6 11M6 1C9 4 9 8 6 11" fill="none" stroke="#fff" stroke-width="1"/></svg>www.q7-platform.example</span>
    <span><svg width="11" height="8" viewBox="0 0 12 9" aria-hidden="true"><rect width="12" height="9" fill="#fff"/><path d="M0 0L6 5 12 0" fill="none" stroke="#d39c1c" stroke-width="1.2"/></svg>hello@q7-platform.example</span>
  </footer>
</main>
</body>
</html>
```